Looking for a professional, clean and crisp business card

I am in the underground utilities industry and am just looking for a really impressive business card. I would like our card to be white with our symbol crisp and clear with it protruding. I also have a business partner that will require his name and info on the card once the design is set. I would like to have our website info on the card which is;
http://granitetrenchco.example/

Contact Information for Business Card

Website, contact name, number and email

```html
<!DOCTYPE html>
<html lang="en">
<head>
<meta charset="utf-8">
<title>Granite Trench Co – Business Card</title>
<link href="https://fonts.googleapis.com/css2?family=Roboto:wght@400;500&display=swap" rel="stylesheet">
<style>
  :root {
    --stage-blue: #4870b8;
    --accent-blue: #6495dd;
    --card-white: #ffffff;
    --ink-dark: #231f20;
    --name-grey: #4a4d52;
    --text-grey: #5f6266;
    --divider-grey: #9a9a9a;
    --ghost-grey: #f3f3f3;
  }
  * { box-sizing: border-box; margin: 0; padding: 0; }
  html, body {
    width: 1200px; height: 895px; overflow: hidden;
    background: var(--stage-blue);
    font-family: "Roboto", Arial, sans-serif;
  }
  .stage { position: relative; width: 1200px; height: 895px; }
  .card {
    position: absolute; left: 307px; width: 577px; height: 340px;
    background: var(--card-white); border-radius: 27px; overflow: hidden;
    box-shadow: 0 10px 30px rgba(30, 50, 100, 0.35);
  }
  .card--front { top: 70px; }
  .card--back { top: 469px; }
  .edge-band {
    position: absolute; left: 130px; width: 310px; height: 5px;
    background: var(--accent-blue);
  }
  .edge-band--top { top: 0; border-radius: 0 0 4px 4px; }
  .edge-band--bottom { bottom: 0; border-radius: 4px 4px 0 0; }
  .brand-name {
    position: absolute; color: var(--ink-dark); font-weight: 500;
    text-align: center; text-transform: uppercase; letter-spacing: 0.06em;
  }
  .brand-name--front {
    left: 0; right: 0; top: 148px; font-size: 32px; line-height: 40px;
  }
  .ghost-circle {
    position: absolute; left: -70px; top: 10px; width: 300px; height: 300px;
    border: 14px solid var(--ghost-grey); border-radius: 50%;
  }
  .brand-name--back {
    left: 80px; width: 102px; top: 156px; font-size: 13px; line-height: 17px;
  }
  .divider {
    position: absolute; left: 250px; top: 100px; width: 2px; height: 157px;
    background: var(--divider-grey);
  }
  .person { position: absolute; left: 276px; top: 82px; }
  .person__name {
    font-size: 22px; font-weight: 500; color: var(--name-grey); line-height: 26px;
  }
  .person__role { font-size: 14px; color: var(--text-grey); line-height: 18px; }
  .contact-list {
    position: absolute; left: 276px; top: 155px; list-style: none;
  }
  .contact-list li {
    display: flex; align-items: flex-start; gap: 9px;
    font-size: 14.5px; color: var(--text-grey); line-height: 17px;
    margin-bottom: 10.5px;
  }
  .contact-list svg { width: 16px; height: 16px; flex: none; fill: var(--accent-blue); }
</style>
</head>
<body>
<main class="stage">
  <section class="card card--front" aria-label="Card front">
    <div class="edge-band edge-band--top"></div>
    <p class="brand-name brand-name--front">Granite Trench Co</p>
    <div class="edge-band edge-band--bottom"></div>
  </section>

  <section class="card card--back" aria-label="Card back">
    <div class="ghost-circle"></div>
    <p class="brand-name brand-name--back">Granite Trench Co</p>
    <div class="divider"></div>
    <div class="person">
      <h1 class="person__name">DEAN HOLLOWAY</h1>
      <p class="person__role">Owner</p>
    </div>
    <ul class="contact-list">
      <li>
        <svg viewBox="0 0 24 24" aria-hidden="true"><path d="M6.6 10.8a15.1 15.1 0 0 0 6.6 6.6l2.2-2.2a1 1 0 0 1 1-.25 11.4 11.4 0 0 0 3.6.57 1 1 0 0 1 1 1V20a1 1 0 0 1-1 1A17 17 0 0 1 3 4a1 1 0 0 1 1-1h3.5a1 1 0 0 1 1 1c0 1.25.2 2.45.57 3.57a1 1 0 0 1-.25 1z"/></svg>
        <span>604-555-0182</span>
      </li>
      <li>
        <svg viewBox="0 0 24 24" aria-hidden="true"><path d="M2 5h20v14H2z M3.5 6.5 12 13l8.5-6.5" stroke="#fff" stroke-width="1.4"/></svg>
        <span>Dean@granitetrenchco.example</span>
      </li>
      <li>
        <svg viewBox="0 0 24 24" aria-hidden="true"><circle cx="12" cy="12" r="10"/><path d="M2 12h20M12 2c3 3 3 17 0 20M12 2c-3 3-3 17 0 20" stroke="#fff" stroke-width="1.4" fill="none"/></svg>
        <span>granitetrenchco.example</span>
      </li>
      <li>
        <svg viewBox="0 0 24 24" aria-hidden="true"><path d="M12 1a8 8 0 0 0-8 8c0 6 8 14 8 14s8-8 8-14a8 8 0 0 0-8-8zm0 11a3 3 0 1 1 0-6 3 3 0 0 1 0 6z"/></svg>
        <span>Fernvale, British Columbia,<br>Canada</span>
      </li>
    </ul>
  </section>
</main>
</body>
</html>
```